New Packaging Design Project

Wine packaging redesign. Retail partner requested a redesign of a private label wine. The old label is attached. Our partner liked the Lantern and Briar label and wanted something similar. There will be a logo added to the top of the label

Went on vacation/holiday

```html
<!DOCTYPE html>
<html lang="en">
<head>
<meta charset="utf-8">
<title>Napa Valley Red Blend – Label Options</title>
<link rel="stylesheet" href="https://fonts.googleapis.com/css2?family=Cinzel:wght@400&family=Jost:wght@300&display=swap">
<style>
  :root {
    --sheet-bg: #ffffff;
    --sheet-frame: #8c8c8c;
    --dark-label-bg: #5b5b5b;
    --gold: #d6b36e;
    --light-label-bg: #ffffff;
    --ink: #2b2b2b;
    --light-label-edge: #6e6e6e;
    --dark-hills: #404040;
    --dark-rows: #8e8a82;
    --dark-field: #3d3d3d;
    --light-hills: #8a8a8a;
    --light-rows: #bfa996;
    --light-field: #8a786c;
  }
  html, body {
    margin: 0;
    padding: 0;
    overflow: hidden;
    background: var(--sheet-bg);
  }
  .sheet {
    position: relative;
    width: 1200px;
    height: 929px;
    overflow: hidden;
    background: var(--sheet-bg);
  }
  .sheet-frame {
    position: absolute;
    left: 1px; top: 1px;
    width: 1196px; height: 925px;
    border: 1px solid var(--sheet-frame);
    box-sizing: border-box;
  }
  .label {
    position: absolute;
    width: 475px;
    overflow: hidden;
    box-sizing: border-box;
    color: var(--label-ink);
    --shift: 0px;
  }
  .label--dark {
    left: 92px; top: 35px; height: 849px;
    background: var(--dark-label-bg);
    --label-ink: var(--gold);
  }
  .label--light {
    left: 651px; top: 49px; height: 835px;
    background: var(--light-label-bg);
    border: 1px solid var(--light-label-edge);
    --label-ink: var(--ink);
    --shift: -14px;
  }
  .label > * {
    position: absolute;
    left: 0; right: 0;
    margin: 0;
    text-align: center;
  }
  .brand-mark {
    top: calc(52px + var(--shift));
    left: 50%; right: auto;
    width: 88px; height: 88px;
    margin-left: -44px;
    border: 2px solid var(--label-ink);
    border-radius: 50%;
    box-sizing: border-box;
    display: flex;
    align-items: center;
    justify-content: center;
    font-family: "Cinzel", serif;
    font-size: 19px;
    letter-spacing: 0.5px;
    text-transform: lowercase;
  }
  .region {
    top: calc(203px + var(--shift));
    font-family: "Cinzel", serif;
    font-weight: 400;
    font-size: 47px;
    letter-spacing: 2px;
    line-height: 56px;
  }
  .wine-style {
    top: calc(330px + var(--shift));
    font-family: "Jost", sans-serif;
    font-weight: 300;
    font-size: 39px;
    line-height: 48px;
    letter-spacing: -0.5px;
    padding-right: 28px;
  }
  .grapes {
    top: calc(394px + var(--shift));
    font-family: "Jost", sans-serif;
    font-weight: 300;
    font-size: 21px;
    line-height: 25px;
    letter-spacing: -0.2px;
    white-space: pre;
  }
  .vintage {
    top: calc(476px + var(--shift));
    font-family: "Jost", sans-serif;
    font-weight: 300;
    font-size: 21px;
    line-height: 26px;
  }
  .landscape {
    top: calc(521px + var(--shift));
    bottom: 0;
  }
  .landscape svg { display: block; width: 100%; height: 100%; }
</style>
</head>
<body>
<main class="sheet">
  <div class="sheet-frame"></div>

  <section class="label label--dark">
    <div class="brand-mark">logo</div>
    <h1 class="region">NAPA VALLEY</h1>
    <h2 class="wine-style">RED BLEND</h2>
    <p class="grapes">MERLOT  / CABERNET SAUVIGNON
CABERNET  FRANC / PETIT VERDOT MALBEC</p>
    <p class="vintage">2018</p>
    <div class="landscape" role="img" aria-label="Illustration of dark hills above gold-striped vineyard rows">
      <svg viewBox="0 0 475 328" preserveAspectRatio="none">
        <defs>
          <linearGradient id="dark-land" x1="0" y1="0" x2="0" y2="1">
            <stop offset="0" stop-color="var(--dark-hills)"/>
            <stop offset="0.45" stop-color="var(--dark-hills)"/>
            <stop offset="0.65" stop-color="var(--dark-rows)"/>
            <stop offset="1" stop-color="var(--dark-field)"/>
          </linearGradient>
        </defs>
        <rect width="475" height="328" fill="url(#dark-land)"/>
      </svg>
    </div>
  </section>

  <section class="label label--light">
    <div class="brand-mark">logo</div>
    <h1 class="region">NAPA VALLEY</h1>
    <h2 class="wine-style">RED BLEND</h2>
    <p class="grapes">MERLOT  / CABERNET SAUVIGNON
CABERNET  FRANC / PETIT VERDOT MALBEC</p>
    <p class="vintage">2018</p>
    <div class="landscape" role="img" aria-label="Illustration of grey hills above taupe vineyard rows">
      <svg viewBox="0 0 475 328" preserveAspectRatio="none">
        <defs>
          <linearGradient id="light-land" x1="0" y1="0" x2="0" y2="1">
            <stop offset="0" stop-color="var(--light-hills)"/>
            <stop offset="0.45" stop-color="var(--light-hills)"/>
            <stop offset="0.65" stop-color="var(--light-rows)"/>
            <stop offset="1" stop-color="var(--light-field)"/>
          </linearGradient>
        </defs>
        <rect width="475" height="328" fill="url(#light-land)"/>
      </svg>
    </div>
  </section>
</main>
</body>
</html>
```